We are looking for an effective ad to recruit work from home Loan Officers for our Mortgage Brokerage.
Use the following text...
Earn Mortgage Income in your sleep. Its as easy as 1, 2, 3.....
1) Solicit Potential Applicants (Word of Mouth, Email, Social Media etc.)
2) Take Complete Applications & Submit Them
3) Wait to Get Paid.......(Avg. $2,500 per closing)
"You open the door, we'll finish the deal"
No Experience Necessary
No Goals or Quotas
No Office Hours / Work from Home Office
...and We Fully Reimburse ALL LICENSING FEES!!
Email Resume to mwelby@brightharborloans.example
Bright Harbor Lending Group, Inc.
947 W Caldwell Avenue, #318
Baltimore, MD 21230
NMLS #731860
www.brightharborloans.example
Phone (800) 555-0142
Licensed Mortgage Broker in MD and DC since 1997
Target Market(s)
Professionals looking to earn part time income at Loan Officers, preferably with strong social media following.
Industry/Entity Type
Loan
Look and feel

```html
<!DOCTYPE html>
<html lang="en">
<head>
<meta charset="utf-8">
<title>Loan Officer Recruitment – Bright Harbor Lending Group</title>
<link href="https://fonts.googleapis.com/css2?family=Oswald:wght@600&family=Open+Sans:wght@400&display=swap" rel="stylesheet">
<style>
  :root {
    --sky-light: #bfe9f2;
    --sky-mid: #8fd8e6;
    --sky-deep: #55c3d4;
    --teal: #2f9ea5;
    --teal-dark: #25898f;
    --charcoal: #3a3d42;
    --silver: #d9dde0;
    --ink: #1f2326;
    --alert: #e8232a;
    --white: #ffffff;
    --navy: #1c3f8c;
  }
  html, body { margin: 0; padding: 0; overflow: hidden; background: #e9eef0; }
  .ad {
    position: relative;
    width: 849px;
    height: 1200px;
    overflow: hidden;
    background: radial-gradient(ellipse at 25% 20%, var(--sky-light) 0%, var(--sky-mid) 55%, var(--sky-deep) 100%);
    font-family: "Open Sans", Arial, sans-serif;
    color: var(--ink);
  }
  .ad__swoosh { position: absolute; inset: 0; }
  .headline {
    position: absolute; left: 33px; top: 84px; margin: 0;
    font-family: "Oswald", "Arial Narrow", sans-serif; font-weight: 600;
    font-size: 36px; line-height: 46px; letter-spacing: 0.5px;
    color: var(--teal); text-transform: uppercase;
  }
  .steps {
    position: absolute; left: 33px; top: 190px; margin: 0; padding: 0;
    list-style: none; font-size: 16px; line-height: 21px;
  }
  .tagline {
    position: absolute; left: 33px; top: 282px; margin: 0;
    font-family: "Oswald", "Arial Narrow", sans-serif; font-weight: 600;
    font-size: 24px; letter-spacing: 0.8px; color: var(--teal); text-transform: uppercase;
    white-space: nowrap;
  }
  .perks {
    position: absolute; left: 33px; top: 331px; margin: 0; padding: 0;
    list-style: none; font-size: 16px; line-height: 21px;
  }
  .perks__fees { margin-left: -7px; margin-top: 6px; }
  .perks__fees strong { font-weight: 400; color: var(--alert); }
  .apply {
    position: absolute; left: 30px; top: 462px; height: 34px;
    padding: 0 20px; border-radius: 17px; background: var(--teal);
    color: var(--white); font-size: 14.5px; line-height: 34px;
    white-space: nowrap;
  }
  .license {
    position: absolute; left: 33px; top: 516px; margin: 0;
    font-size: 22px; line-height: 28px;
  }
  .contact {
    position: absolute; left: 34px; top: 596px; margin: 0;
    font-style: normal; font-size: 16px; line-height: 20.5px;
  }
  .brand-tile {
    position: absolute; left: 32px; top: 730px; width: 164px; height: 107px;
    background: var(--white); display: flex; align-items: center; justify-content: center;
    text-align: center; box-sizing: border-box; padding: 10px;
    font-size: 14px; line-height: 18px; color: var(--navy);
  }
  .model-photo {
    position: absolute; left: 208px; top: 448px; width: 530px; height: 752px;
    background: radial-gradient(ellipse at 55% 40%, #f3efe9 0%, #e4dcd3 45%, rgba(228,220,211,0) 72%);
  }
  .social-badge {
    position: absolute; left: 648px; top: 1122px; width: 176px; height: 58px;
    box-sizing: border-box; border: 3px solid var(--navy); background: var(--white);
    display: flex; align-items: center; justify-content: center; gap: 7px;
    padding: 0 8px; font-size: 13px; color: var(--navy); white-space: nowrap;
  }
  .social-badge__mark { flex: none; width: 12px; height: 12px; background: var(--navy); }
</style>
</head>
<body>
<main class="ad">
  <svg class="ad__swoosh" width="849" height="1200" viewBox="0 0 849 1200" aria-hidden="true">
    <path d="M430,0 C690,40 820,250 849,430 L849,0 Z" fill="var(--silver)"/>
    <path d="M470,0 C720,50 830,250 849,400 L849,0 Z" fill="var(--charcoal)"/>
    <path d="M540,0 C760,70 840,260 849,380 L849,0 Z" fill="var(--white)"/>
    <path d="M575,0 C780,80 845,260 849,360 L849,0 Z" fill="var(--teal)"/>
    <path d="M0,820 C30,1010 170,1140 320,1200 L0,1200 Z" fill="var(--silver)"/>
    <path d="M0,860 C40,1030 160,1140 290,1200 L0,1200 Z" fill="var(--charcoal)"/>
    <path d="M0,890 C50,1045 160,1140 270,1200 L0,1200 Z" fill="var(--white)"/>
    <path d="M0,910 C55,1055 160,1145 250,1200 L0,1200 Z" fill="var(--teal)"/>
  </svg>

  <div class="model-photo" role="img" aria-label="Photo of a smiling red-haired woman in red glasses and a white shirt, holding a fan of dollar bills and pointing upward"></div>

  <h1 class="headline">Earn mortgage income in<br>your sleep. Its as easy as 1, 2, 3.....</h1>

  <ol class="steps">
    <li>1) Solicit Potential Applicants (Word of Mouth, Email, Social Media etc.)</li>
    <li>2) Take Complete Applications &amp; Submit Them</li>
    <li>3) Wait to Get Paid.......(Avg. $2,500 per closing)</li>
  </ol>

  <p class="tagline">"You open the door, we'll finish the deal"</p>

  <ul class="perks">
    <li>No Experience Necessary</li>
    <li>No Goals or Quotas</li>
    <li>No Office Hours / Work from Home Office</li>
    <li class="perks__fees">...and We Fully Reimburse <strong>ALL LICENSING FEES!!</strong></li>
  </ul>

  <div class="apply">Email Resume to mwelby@brightharborloans.example</div>

  <p class="license">Licensed Mortgage Broker<br>in MD and DC since 1997</p>

  <address class="contact">
    Bright Harbor Lending Group, Inc.<br>
    947 W Caldwell Avenue, #318<br>
    Baltimore, MD 21230<br>
    NMLS #731860<br>
    www.brightharborloans.example<br>
    Phone (800) 555-0142
  </address>

  <div class="brand-tile">Bright Harbor Lending Group</div>

  <div class="social-badge"><span class="social-badge__mark"></span>Like us on Circlepage</div>
</main>
</body>
</html>
```